Postcard design for functional fitness festival sporting event

We need a postcard designed that will act as a marketing lever for members of existing gyms. It will promote a sporting event we are running and it is planned that existing gyms in 3 x States within Australia will have these on their reception desks, hand them out to members etc. by way of promoting the event. The look and feel of the postcard must be inline with the branding as per our website and should convey a trendy retro, fun and exciting feel.

All photos on the website are available for use with this postcard.

Note: this is not a real postcard that will be sent in the mail - we will send boxes of 200 to each gym so they don't require space for a stamp or address

Target Market(s)

Members of PulseRig and K27 gyms in New South Wales, ACT and Victoria [Australia]. This means 30-55, equally mixed between male and female, high income earners with children.

Industry/Entity Type

Fitness

Font styles to use
Sans Serif

Requirements
Must have
• The branding, look and feel should be aligned with the website www.thekestrelcup.com.au
• They must be eye-catching... imagine they are just lying on the reception desk at a gym - we want them to catch the eye.
• The Kestrel Cup logo coupled with the description, 'Australia's Premier Functional Fitness Festival' should be featured.
• This descriptin can be used: THE KESTREL CUP is the premier Functional Fitness Festival in Australia where the fittest everyday athletes and teams from around the country travel to Jervis Bay in NSW to showcase the heart and dedication required to compete against the most determined weekend warriors…
• Other pertinent info includes:
• The dates of the event = 10th & 11th November 2018
• Where = Jervis Bay, NSW
• There are basically 4 x separate categories within the event we want the postcard reader to be aware of - as below:
• Individuals and Team entries available
• Strongman and Strongwoman competition [please see the logo for the ANVIL competition on the website]
• Juniors category
• Prize money = $1,000
• The main Call To Action that the postcard(s) should promote is to 'Register Now'

```html
<!DOCTYPE html>
<html lang="en">
<head>
<meta charset="utf-8">
<title>The Kestrel Cup – Postcard</title>
<link href="https://fonts.googleapis.com/css2?family=Montserrat:wght@300;800;900&family=Lato:wght@400;700&family=Oswald:wght@600&family=Roboto:wght@700;900&display=swap" rel="stylesheet">
<style>
:root{
  --navy:#2c2c6c;
  --navy-deep:#24245c;
  --orange:#f7941d;
  --blue:#5b86c2;
  --white:#ffffff;
  --ink:#111111;
  --photo-light:#a9a9a9;
  --photo-dark:#4a4a4a;
}
*{margin:0;padding:0;box-sizing:border-box}
html,body{width:1200px;height:1200px;overflow:hidden;background:var(--white)}
body{position:relative;font-family:"Lato",sans-serif}
.card{position:absolute;left:234px;width:732px;height:566px;overflow:hidden;box-shadow:4px 6px 10px rgba(0,0,0,.35)}
.card--front{top:22px}
.card--back{top:612px;background:var(--navy)}
.card p,.card h1,.card h2,.card h3,.card span{white-space:nowrap}

/* front */
.front-photo{position:absolute;inset:0;background:linear-gradient(160deg,var(--photo-light) 0%,#7d7d7d 45%,var(--photo-dark) 100%)}
.brand-mark{position:absolute;left:30px;top:44px;display:flex;align-items:center;gap:10px}
.brand-mark__dot{width:22px;height:22px;border-radius:50%;background:var(--orange)}
.brand-mark__name{font-family:"Montserrat",sans-serif;font-weight:800;font-size:22px;color:var(--white);letter-spacing:.5px}
.ribbon{position:absolute;left:0}
.ribbon--place{top:186px;width:256px;height:50px}
.ribbon--register{top:264px;width:272px;height:68px}
.ribbon__bg{position:absolute;left:0;top:0}
.ribbon__place-text{position:absolute;left:62px;top:12px;font-family:"Montserrat",sans-serif;font-weight:300;font-size:20px;color:var(--white);letter-spacing:.3px}
.ribbon__pin{position:absolute;left:28px;top:13px}
.ribbon__cta{position:absolute;left:25px;top:8px;font-family:"Montserrat",sans-serif;font-weight:900;font-size:26px;color:var(--navy)}
.ribbon__url{position:absolute;left:25px;top:38px;font-size:17px;color:var(--white)}
.front-band{position:absolute;left:0;top:392px;width:732px;height:174px}
.front-title{position:absolute;top:424px;width:100%;text-align:center;font-family:"Montserrat",sans-serif;font-weight:900;font-size:34px;color:var(--white);letter-spacing:.3px}
.front-dates{position:absolute;top:465px;width:100%;text-align:center;font-family:"Montserrat",sans-serif;font-weight:300;font-size:25px;color:var(--white);letter-spacing:1px}
.front-year{position:absolute;top:496px;width:100%;text-align:center;font-family:"Montserrat",sans-serif;font-weight:900;font-size:50px;color:var(--white)}
.front-year-rule{position:absolute;top:516px;height:2px;width:68px;background:var(--white)}

/* back */
.back-photo{position:absolute;inset:0;background:linear-gradient(180deg,var(--navy) 0%,#3a3c7c 55%,var(--navy-deep) 100%)}
.back-kicker{position:absolute;left:30px;top:16px;font-family:"Roboto",sans-serif;font-weight:900;font-size:34px;line-height:40px;color:var(--white)}
.back-headline{position:absolute;left:28px;top:58px;font-family:"Roboto",sans-serif;font-weight:900;font-size:66px;line-height:70px;color:var(--white);letter-spacing:-.5px}
.back-intro{position:absolute;left:34px;top:134px;width:672px;font-size:15.5px;line-height:19px;color:var(--white);text-align:justify;white-space:normal!important}
.categories-title{position:absolute;left:30px;top:192px;font-family:"Oswald",sans-serif;font-weight:600;font-size:25px;color:var(--white);border-bottom:2px solid var(--white);padding-right:8px;line-height:1.2}
.category{position:absolute;font-size:16px;color:var(--white);display:flex;align-items:center;gap:8px}
.category::before{content:"";width:7px;height:7px;border-radius:50%;background:var(--orange)}
.prize{position:absolute;left:124px;top:293px;width:484px;height:190px;background:var(--orange);border-radius:12px}
.prize__frame{position:absolute;inset:9px;border:2px dashed var(--white);border-radius:10px}
.prize__label{position:absolute;top:10px;width:100%;text-align:center;font-family:"Roboto",sans-serif;font-weight:700;font-size:48px;color:var(--ink)}
.prize__amount{position:absolute;top:68px;width:100%;text-align:center;font-family:"Montserrat",sans-serif;font-weight:900;font-size:94px;color:var(--ink);letter-spacing:-3px}
.contact{position:absolute;font-size:15px;color:var(--white);display:flex;align-items:center;gap:10px}
.contact__mark{width:12px;height:12px;border-radius:50%;background:var(--orange);flex:none}
</style>
</head>
<body>

<section class="card card--front">
  <div class="front-photo" role="img" aria-label="Black and white photo of a bearded athlete pulling a heavy rope on grass in front of a crowd behind barriers"></div>

  <div class="brand-mark">
    <span class="brand-mark__dot"></span>
    <span class="brand-mark__name">THE KESTREL CUP</span>
  </div>

  <div class="ribbon ribbon--place">
    <svg class="ribbon__bg" width="256" height="50" viewBox="0 0 256 50">
      <polygon points="0,1 250,1 240,25 250,49 0,49" fill="#2c2c6c" stroke="#f7941d" stroke-width="2"/>
    </svg>
    <svg class="ribbon__pin" width="18" height="24" viewBox="0 0 18 24">
      <path d="M9 1C4.6 1 1 4.5 1 8.8 1 14.5 9 23 9 23s8-8.5 8-14.2C17 4.5 13.4 1 9 1z" fill="none" stroke="#fff" stroke-width="1.8"/>
      <circle cx="9" cy="9" r="3" fill="#fff"/>
    </svg>
    <span class="ribbon__place-text">JERVIS BAY, NSW</span>
  </div>

  <div class="ribbon ribbon--register">
    <svg class="ribbon__bg" width="272" height="68" viewBox="0 0 272 68">
      <polygon points="0,1 264,1 252,34 264,67 0,67" fill="#f7941d" stroke="#5b86c2" stroke-width="2"/>
    </svg>
    <span class="ribbon__cta">REGISTER NOW</span>
    <span class="ribbon__url">www.thekestrelcup.com.au</span>
  </div>

  <svg class="front-band" viewBox="0 0 732 174" preserveAspectRatio="none">
    <path d="M0 30 Q366 -4 732 30 L732 174 L0 174 Z" fill="#5b86c2" opacity=".93"/>
    <path d="M0 30 Q366 -4 732 30" fill="none" stroke="#f7941d" stroke-width="3"/>
  </svg>
  <h1 class="front-title">FUNCTIONAL FITNESS FESTIVAL</h1>
  <p class="front-dates">10TH &amp; 11TH NOVEMBER</p>
  <span class="front-year-rule" style="left:212px"></span>
  <p class="front-year">2018</p>
  <span class="front-year-rule" style="left:452px"></span>
</section>

<section class="card card--back">
  <div class="back-photo" role="img" aria-label="Navy tinted photo of athletes running during a competition"></div>

  <h2 class="back-kicker">AUSTRALIA'S PREMIER FUNCTIONAL</h2>
  <h2 class="back-headline">FITNESS FESTIVAL</h2>
  <p class="back-intro">THE KESTREL CUP is the premier Functional Fitness Festival in Australia where the fittest everyday athletes and teams from around the country travel to Jervis Bay in NSW to showcase the heart and dedication required to compete against the most determined weekend warriors…</p>

  <h3 class="categories-title">EVENT CATEGORIES:</h3>
  <p class="category" style="left:30px;top:236px">Individuals and Team entries available</p>
  <p class="category" style="left:382px;top:236px">Strongman and Strongwoman competition</p>
  <p class="category" style="left:289px;top:259px">Juniors category</p>

  <div class="prize">
    <div class="prize__frame"></div>
    <p class="prize__label">Prize money</p>
    <p class="prize__amount">$1,000</p>
  </div>

  <p class="contact" style="left:30px;top:500px"><span class="contact__mark"></span>www.thekestrelcup.com.au</p>
  <p class="contact" style="left:30px;top:530px"><span class="contact__mark"></span>www.friendspace.com/Thekestrelcup</p>
  <p class="contact" style="left:396px;top:504px"><span class="contact__mark"></span>www.snapframe.com/thekestrelcup</p>
  <p class="contact" style="left:396px;top:528px"><span class="contact__mark"></span>www.streamtube.com/channel/thekestrelcup</p>
</section>

</body>
</html>
```